Web Design Project

We need a web design for a new company that we started called TALMO CNG. TALMO CNG is a company that will build, own and operate compressed natural gas fueling stations throughout the United States. Our primary customers are Trucking companies and the stations will be built for semi trucks. CNG is better for the environment than diesel fuel, and will save trucking companies loads of money. It is also a domestic product which means that it will create American jobs and help America become energy independent. I have attached a logo that we are using. We dont need to stay with this logo persay, but it is what we have for now. We have a video on Youtube that shows a bit of what we are doing. just search for TALMO CNG. TALMO CNG is a sister company of Haulbright of Arizona,www.hbrtqx.example and a nationwide distributor of VANTO RIG, www.vantorig.example. We will need links to these sites. Please make any pictures of trucks Haulbright trucks, and please do not use pictures of cabover trucks.

Target Market(s)

The target market are truck drivers and truckers.

Industry/Entity Type

Environment

Requirements
Must have
• Map showing station locations, a page with industry news, a page with a savings calculator (we can code the calculator) Site should have links to

```html
<!DOCTYPE html>
<html lang="en">
<head>
<meta charset="utf-8">
<title>TALMO CNG</title>
<link href="https://fonts.googleapis.com/css2?family=Source+Sans+3:wght@400;600&family=PT+Sans:wght@400;700&display=swap" rel="stylesheet">
<style>
:root{
  --green:#4aa51c;
  --brand:#22d63a;
  --blue:#3a95cf;
  --blue-light:#5fb4e8;
  --nav-bg:#d9dfd8;
  --nav-active:#c3c9c2;
  --nav-line:#c6ccc5;
  --text:#333;
  --gold:#f2b630;
}
*{box-sizing:border-box;margin:0;padding:0}
html,body{width:960px;height:1200px;overflow:hidden;background:#fff}
body{position:relative;font-family:"PT Sans",sans-serif;color:var(--text)}
.abs{position:absolute}

.follow{left:692px;top:12px;font:600 12px "Source Sans 3",sans-serif;color:var(--green)}
.social{left:778px;top:10px;display:flex;gap:7px}
.social span{width:20px;height:20px;border-radius:4px;display:block}
.logo{left:90px;top:38px;font:600 38px/1 "Source Sans 3",sans-serif;color:var(--brand);letter-spacing:-1px}
.tagline{right:86px;top:56px;font:400 21px "Source Sans 3",sans-serif;color:var(--blue)}

.side-nav{left:80px;top:95px;width:227px;height:308px;background:var(--nav-bg);border-radius:4px;overflow:hidden;list-style:none}
.side-nav li{height:33px;border-bottom:1px solid var(--nav-line);display:flex;align-items:center;padding-left:32px;font:400 11px "Source Sans 3",sans-serif;color:#222;gap:10px}
.side-nav li:first-child{height:40px;background:var(--nav-active)}
.side-nav li:last-child{border-bottom:none}
.side-nav svg{width:9px;height:9px}

.hero{left:316px;top:95px;width:563px;height:308px;border-radius:4px;
  background:
    radial-gradient(ellipse 90px 120px at 82% 75%, rgba(25,160,60,.55), transparent 70%),
    radial-gradient(ellipse 180px 140px at 38% 62%, #b3201f 0%, rgba(150,25,25,.8) 45%, transparent 75%),
    radial-gradient(ellipse 140px 130px at 85% 55%, #1d1b1c 0%, rgba(30,28,30,.7) 50%, transparent 80%),
    radial-gradient(ellipse 160px 120px at 10% 60%, #dcdcdc 0%, transparent 75%),
    linear-gradient(180deg,#f3f4f2 0%,#d9dad6 30%,#8e8b86 70%,#4e4c4a 100%);}

.search-bar{left:80px;top:409px;width:799px;height:40px;border-radius:4px;background:linear-gradient(#3a3a3a,#0d0d0d)}
.search-input{left:9px;top:10px;width:270px;height:17px;background:#f5f5f5}
.search-label{left:289px;top:12px;font:400 12px "Source Sans 3",sans-serif;color:#fff}
.call{right:16px;top:8px;font:400 19px "Source Sans 3",sans-serif;color:var(--gold)}

.panel-head{left:81px;width:228px;height:30px;border-radius:4px;background:linear-gradient(var(--blue-light),var(--blue));color:#fff;font:400 15px "Source Sans 3",sans-serif;padding:5px 17px}
.news{left:86px;top:500px;width:223px;list-style:none}
.news li{height:78px;border-bottom:1px solid #ccc;position:relative;margin-bottom:11px}
.news .thumb{position:absolute;left:1px;top:2px;width:51px;height:48px}
.news p{position:absolute;left:67px;top:6px;font-size:9.5px;line-height:16px;color:#444;width:128px;letter-spacing:.2px}
.news .date,.news .more{position:absolute;top:62px;font-size:9.5px;color:var(--green);letter-spacing:.5px;line-height:1}
.news .date{left:0}.news .more{right:6px}

.title{font:400 20px "Source Sans 3",sans-serif;color:var(--green)}
.welcome{left:324px;top:460px}
.copy{font-size:9.6px;line-height:16px;color:#222;text-align:justify;letter-spacing:.25px}
.copy-a{left:325px;top:497px;width:273px}
.copy-b{left:325px;top:686px;width:550px}
.station-photo{left:624px;top:494px;width:254px;height:170px;
  background:
    radial-gradient(ellipse 70px 50px at 75% 62%, #1f8c3a 0%, transparent 80%),
    radial-gradient(ellipse 50px 40px at 30% 65%, #f2f2f2 0%, transparent 80%),
    radial-gradient(ellipse 40px 30px at 55% 85%, rgba(230,200,40,.6), transparent 80%),
    linear-gradient(180deg,#4d5053 0%,#4d5053 18%,#9aa2a0 30%,#6d756f 60%,#3d4140 100%);}

.video-title{left:83px;top:796px;font:400 20px "Source Sans 3",sans-serif;color:var(--blue)}
.video-box{left:80px;top:831px;width:230px;height:168px;border:1px solid #ddd;border-radius:4px;background:#f7f7f7}
.video-frame{left:6px;top:10px;width:217px;height:132px;background:linear-gradient(120deg,#4ee08a 0%,#7de6a0 45%,#66d0e0 100%)}
.video-controls{left:6px;top:141px;width:217px;height:9px;background:#111}

.subscribe{left:81px;top:1014px;width:228px;height:76px;border-radius:4px;background:linear-gradient(var(--blue-light),var(--blue))}
.subscribe h3{position:absolute;left:8px;top:6px;font:400 15px "Source Sans 3",sans-serif;color:#fff}
.subscribe .email{position:absolute;left:10px;top:28px;width:208px;height:19px;background:#fff;font-size:9.5px;color:#aaa;padding:3px 13px}
.subscribe .submit{position:absolute;left:135px;top:54px;width:83px;height:18px;border:1px solid #fff;border-radius:4px;background:linear-gradient(#6cc0f0,#2a86c8);color:#fff;font:600 11px "Source Sans 3",sans-serif;text-align:center;line-height:16px}

.map-title{left:324px;top:793px}
.map{left:324px;top:831px;width:555px;height:260px;border:1px solid #ddd;
  background:
    radial-gradient(ellipse 90px 140px at 6% 40%, #b9cf9d 0%, transparent 80%),
    radial-gradient(ellipse 30px 22px at 32% 22%, #b7d6a0 0%, transparent 90%),
    linear-gradient(90deg,#d4e0bf 0%,#ebe9df 30%,#f1efe8 100%);}

.footer{left:80px;top:1107px;width:799px;height:40px;border-radius:4px;background:linear-gradient(#3a3a3a,#0d0d0d);display:flex;align-items:center;padding:0 18px;font:400 10px "Source Sans 3",sans-serif;color:#ddd}
.footer nav span{margin:0 12px}
.footer nav span.sep{margin:0}
.footer .copyright{margin-left:auto;font-size:9px}
</style>
</head>
<body>

<div class="abs follow">Follow us on :</div>
<div class="abs social" aria-label="Social links">
  <span style="background:#3b5a98"></span><span style="background:#52b6e6"></span><span style="background:#444"></span><span style="background:#f08a2a"></span>
</div>
<div class="abs logo">TALMO CNG</div>
<div class="abs tagline">Will Save Trucking Companies Loads of Money</div>

<ul class="abs side-nav">
  <li><svg viewBox="0 0 9 9"><rect width="9" height="9" rx="2" fill="#777"/><path d="M4.5 2v5M2 4.5h5" stroke="#f2c230" stroke-width="1.4"/></svg>HOME</li>
  <li><svg viewBox="0 0 9 9"><rect width="9" height="9" rx="2" fill="#888"/><path d="M4.5 2v5M2 4.5h5" stroke="#fff" stroke-width="1.4"/></svg>ABOUT US</li>
  <li><svg viewBox="0 0 9 9"><rect width="9" height="9" rx="2" fill="#888"/><path d="M4.5 2v5M2 4.5h5" stroke="#fff" stroke-width="1.4"/></svg>WHATS NEW</li>
  <li><svg viewBox="0 0 9 9"><rect width="9" height="9" rx="2" fill="#888"/><path d="M4.5 2v5M2 4.5h5" stroke="#fff" stroke-width="1.4"/></svg>TEAM</li>
  <li><svg viewBox="0 0 9 9"><rect width="9" height="9" rx="2" fill="#888"/><path d="M4.5 2v5M2 4.5h5" stroke="#fff" stroke-width="1.4"/></svg>FOCUS</li>
  <li><svg viewBox="0 0 9 9"><rect width="9" height="9" rx="2" fill="#888"/><path d="M4.5 2v5M2 4.5h5" stroke="#fff" stroke-width="1.4"/></svg>INDUSTRIES</li>
  <li><svg viewBox="0 0 9 9"><rect width="9" height="9" rx="2" fill="#888"/><path d="M4.5 2v5M2 4.5h5" stroke="#fff" stroke-width="1.4"/></svg>SAVINGS</li>
  <li><svg viewBox="0 0 9 9"><rect width="9" height="9" rx="2" fill="#888"/><path d="M4.5 2v5M2 4.5h5" stroke="#fff" stroke-width="1.4"/></svg>STATION LOCATION</li>
  <li><svg viewBox="0 0 9 9"><rect width="9" height="9" rx="2" fill="#888"/><path d="M4.5 2v5M2 4.5h5" stroke="#fff" stroke-width="1.4"/></svg>CONTACT US</li>
</ul>

<div class="abs hero" role="img" aria-label="Photo of a red semi truck and a dark semi truck refuelling under a CNG station canopy"></div>

<div class="abs search-bar">
  <div class="abs search-input"></div>
  <div class="abs search-label">Search</div>
  <div class="abs call">Call us now: 1800-55-0100</div>
</div>

<div class="abs panel-head" style="top:456px">Industry News</div>
<ul class="abs news">
  <li><div class="thumb" role="img" aria-label="Fuel station photo" style="background:linear-gradient(#6b7f6e,#a9b1aa 50%,#4f5a52)"></div><p>Lorem ipsum dolor sit amet, consectetur adipisicing elit, sedeiu</p><span class="date">02 - 01 - 2013</span><span class="more">Readmore...</span></li>
  <li><div class="thumb" role="img" aria-label="Compressor equipment photo" style="background:linear-gradient(#5d7186,#8ea3b5 50%,#3e4a56)"></div><p>Lorem ipsum dolor sit amet, consectetur adipisicing elit, sedeiu</p><span class="date">02 - 01 - 2013</span><span class="more">Readmore...</span></li>
  <li><div class="thumb" role="img" aria-label="Truck at fuel pump photo" style="background:linear-gradient(#c9cfcc,#4f9a5a 55%,#5b605c)"></div><p>Lorem ipsum dolor sit amet, consectetur adipisicing elit, sedeiu</p><span class="date">02 - 01 - 2013</span><span class="more">Readmore...</span></li>
</ul>

<h1 class="abs title welcome">Welcome to our website</h1>
<p class="abs copy copy-a">Lorem ipsum dolor sit amet, consectetur adipisicing elit, sed do eiusmod tempor incididunt ut labore et dolore magna aliqua. Ut enim ad minim veniam, quis nostrud exercitation ullamco laboris nisi ut aliquip ex ea commodo consequat. Lorem ipsum dolor sit amet, consectetur adipisicing elit, sed do eiusmod tempor incididunt ut labore et dolore magna aliqua. Ut enim ad minim veniam, quis nostrud exercitation ullamco laboris nisti ut aliquip ex ea commodo consequat.Lorem ipsum dolor sit amet, consectetur ex ea commodo consequat.Lorem ipsum dolor sit amet, consectetur</p>
<div class="abs station-photo" role="img" aria-label="Photo of refuse trucks at a CNG fueling station"></div>
<p class="abs copy copy-b">Lorem ipsum dolor sit amet, consectetur adipisicing elit, sed do eiusmod tempor incididunt ut labore et dolore magna aliqua. Ut enim ad minim veniam, quis nostrud exercitation ullamco laboris nisi ut aliquip ex ea commodo consequat. Lorem ipsum dolor sit amet, consectetur adipisicing elit, sed do eiusmod tempor incididunt ut labore et dolore magna aliqua. Ut enim ad minim veniam, quis nostrud exercitation ullamco laboris nisi ut aliquip ex ea commodo consequat. ullamco laboris nisi ut aliquip ex ea commodo consequat</p>

<h2 class="abs video-title">Video</h2>
<div class="abs video-box">
  <div class="abs video-frame" role="img" aria-label="Company video still"></div>
  <div class="abs video-controls"></div>
</div>

<div class="abs subscribe">
  <h3>Subscribe News Letter</h3>
  <div class="email">Enter email address</div>
  <div class="submit">Submit</div>
</div>

<h2 class="abs title map-title">Location Map</h2>
<div class="abs map" role="img" aria-label="Road map of Colorado, Nebraska and Kansas showing station locations"></div>

<footer class="abs footer">
  <nav><span style="margin-left:0">Home</span><span class="sep">|</span><span>About Us</span><span class="sep">|</span><span>Whats New</span><span class="sep">|</span><span>Team</span><span class="sep">|</span><span>Focus</span><span class="sep">|</span><span>Industries</span><span class="sep">|</span><span>Savings</span><span class="sep">|</span><span>Contact Us</span></nav>
  <div class="copyright">Copyright © 2013 Talmo-CNG</div>
</footer>

</body>
</html>
```